Instagram post design for clothing brand

please see the attached design brief PDF

I will raise the budget for designs so I want to provide more submissions and designs
I have extended the deadline for submissions by one week extra

Requirements
Must have
• I want t-shirt mockup so I can put any design I want

```html
<!DOCTYPE html>
<html lang="en">
<head>
<meta charset="utf-8">
<title>Tolvara – Instagram Post Set</title>
<link href="https://fonts.googleapis.com/css2?family=Teko:wght@300;500;600&display=swap" rel="stylesheet">
<style>
  :root {
    --cream: #fff2c4;
    --teal: #00807a;
    --paper: #f9f9fa;
    --ink: #0a0a0a;
    --brand-blue: #1c95d6;
    --beige: #d6c4b7;
    --shirt-dark: #1c1c1c;
    --tee-white: #e9e9ee;
  }
  * { margin: 0; padding: 0; box-sizing: border-box; }
  html, body { width: 1200px; height: 849px; overflow: hidden; }
  body {
    background: var(--cream);
    font-family: "Teko", sans-serif;
    position: relative;
  }
  .post {
    position: absolute;
    width: 349px;
    height: 620px;
    overflow: hidden;
    background: var(--paper);
    border: 1px solid #555;
  }
  .post--product { left: 46px; top: 108px; }
  .post--mockup { left: 436px; top: 105px; }
  .post--blank { left: 803px; top: 101px; height: 624px; background: var(--teal); }
  .post svg.layers { position: absolute; inset: 0; width: 100%; height: 100%; }
  .torn { filter: drop-shadow(0 3px 3px rgba(0,0,0,.28)); }

  .brand {
    position: absolute;
    width: 60px;
    display: flex;
    flex-direction: column;
    align-items: center;
    gap: 5px;
  }
  .brand__square { width: 43px; height: 51px; background: var(--ink); }
  .brand__name {
    font-weight: 500;
    font-size: 22px;
    line-height: 1;
    color: var(--brand-blue);
    letter-spacing: 0.3px;
    white-space: nowrap;
  }
  .post--product .brand--corner { left: 15px; top: 33px; }
  .post--mockup .brand--corner { left: 14px; top: 33px; }
  .post--blank .brand--corner { left: 264px; top: 519px; }

  .tee-photo {
    position: absolute;
    left: 32px; top: 198px;
    width: 293px; height: 295px;
    border-radius: 4px;
    background: linear-gradient(160deg, #ffffff 0%, var(--tee-white) 100%);
    box-shadow: 0 5px 10px rgba(0,0,0,.28);
  }
  .post--product .brand--print { left: 50%; top: 271px; transform: translateX(-50%); }

  .model-photo {
    position: absolute;
    left: 0; top: 60px;
    width: 349px; height: 560px;
    background: linear-gradient(90deg, var(--beige) 0%, var(--shirt-dark) 12%, var(--shirt-dark) 88%, var(--beige) 100%);
  }
  .mockup-frame {
    position: absolute;
    left: 16px; top: 28px; width: 319px; height: 574px;
    border: 1px solid rgba(255,255,255,.85);
    outline: 1px solid rgba(255,255,255,.6);
    outline-offset: -4px;
  }
  .design-slot {
    position: absolute;
    left: 0; right: 0; top: 210px;
    text-align: center;
    color: #fff;
    line-height: 0.9;
  }
  .design-slot__paste, .design-slot__here { font-weight: 300; font-size: 38px; letter-spacing: 1px; }
  .design-slot__design { font-weight: 600; font-size: 48px; }
</style>
</head>
<body>

  <section class="post post--product">
    <svg class="layers" viewBox="0 0 349 620" preserveAspectRatio="none" aria-hidden="true">
      <path class="torn" fill="#00807a" d="M0,140 L10,137 20,143 30,150 40,158 46,152 55,147 65,140 78,133 90,125 100,118 108,112 118,115 125,112 135,106 145,98 160,92 175,93 190,97 205,95 220,104 235,114 245,120 260,116 275,110 290,112 305,104 320,107 335,100 349,95 L349,567 330,565 310,567 290,572 270,574 250,578 230,582 210,581 190,583 170,585 150,590 130,592 110,592 90,595 70,597 50,599 30,601 15,601 0,603 Z"/>
    </svg>
    <div class="brand brand--corner"><span class="brand__square"></span><span class="brand__name">TOLVARA</span></div>
    <div class="tee-photo" role="img" aria-label="Product photo of a plain white t-shirt"></div>
    <div class="brand brand--print"><span class="brand__square"></span><span class="brand__name">TOLVARA</span></div>
  </section>

  <section class="post post--mockup">
    <div class="model-photo" role="img" aria-label="Photo of a man wearing a black t-shirt and jeans against a beige wall"></div>
    <svg class="layers" viewBox="0 0 349 620" preserveAspectRatio="none" aria-hidden="true">
      <path class="torn" fill="#f9f9fa" d="M0,0 H349 V100 L335,103 320,108 305,112 290,117 275,119 260,118 245,115 230,110 215,105 205,99 195,97 185,99 175,96 165,96 160,92 150,88 145,92 138,100 130,110 118,116 100,121 85,126 70,132 55,140 45,148 38,150 30,145 20,140 10,137 0,139 Z"/>
    </svg>
    <div class="mockup-frame"></div>
    <div class="brand brand--corner"><span class="brand__square"></span><span class="brand__name">TOLVARA</span></div>
    <div class="design-slot">
      <div class="design-slot__paste">PASTE</div>
      <div class="design-slot__design">DESIGN</div>
      <div class="design-slot__here">HERE</div>
    </div>
  </section>

  <section class="post post--blank">
    <svg class="layers" viewBox="0 0 349 624" preserveAspectRatio="none" aria-hidden="true">
      <path class="torn" fill="#f9f9fa" d="M54,79 H307 V172 L290,171 270,172 250,174 230,174 210,176 190,177 170,178 150,177 130,179 110,180 90,180 70,181 54,177 Z"/>
      <path class="torn" fill="#f9f9fa" d="M0,510 L15,505 30,498 45,494 60,490 68,493 80,488 95,491 105,496 115,504 125,508 140,507 155,512 165,516 175,510 185,503 200,497 215,495 225,488 235,480 245,472 258,462 270,455 280,460 295,465 305,472 320,473 335,465 349,460 V624 H0 Z"/>
    </svg>
    <div class="brand brand--corner"><span class="brand__square"></span><span class="brand__name">TOLVARA</span></div>
  </section>

</body>
</html>
```